" O nome Valtessora significa dentro do movimento. A clínica tem como carro chefe um trabalho chamado de videoanálise de movimento. Usamos um software para realizar análise de marcha, corrida, salto, estabilidade, flexibilidade entre outros. Identificamos alteraçoes no movimento que possam ser a causa de dor ou diminmuiçao no rendimento físico-funcional. Alteraçoes identificadas entramos com a reabilitaçao usando Pilates, RPG, Hidroterapia, Treinamento Funcional, Osteopatia entre outros. Nosso foco: resultados! "

```html
<!DOCTYPE html>
<html lang="pt-BR">
<head>
<meta charset="UTF-8">
<title>Valtessora – Papel Timbrado</title>
<link rel="stylesheet" href="https://fonts.googleapis.com/css2?family=Roboto:wght@400;700&display=swap">
<style>
  :root {
    --backdrop: #e6e6e6;
    --paper: #ffffff;
    --brand-navy: #1f3f8c;
    --text-grey: #6f6f6f;
    --rule-grey: #a5a5a5;
    --mark-grey: #efefef;
  }
  * { margin: 0; padding: 0; box-sizing: border-box; }
  html, body {
    width: 1200px;
    height: 1200px;
    overflow: hidden;
    background: var(--backdrop);
    font-family: "Roboto", Arial, sans-serif;
  }
  .canvas {
    width: 1200px;
    height: 1200px;
    display: flex;
    align-items: center;
    justify-content: center;
  }
  .letterhead {
    position: relative;
    width: 764px;
    height: 1080px;
    background: var(--paper);
    box-shadow: 0 6px 18px rgba(0, 0, 0, 0.08);
  }
  .brand {
    position: absolute;
    top: 52px;
    left: 46px;
    display: flex;
    flex-direction: column;
    gap: 6px;
  }
  .brand-line {
    display: flex;
    align-items: center;
    gap: 10px;
  }
  .brand-dot {
    width: 22px;
    height: 22px;
    border-radius: 50%;
    background: var(--brand-navy);
  }
  .brand-name {
    font-size: 32px;
    font-weight: 700;
    color: var(--brand-navy);
    letter-spacing: -0.5px;
    line-height: 1;
  }
  .brand-tagline {
    font-size: 9px;
    color: var(--text-grey);
    letter-spacing: 0.4px;
    padding-left: 32px;
  }
  .contact-block {
    position: absolute;
    top: 44px;
    left: 522px;
    padding-left: 10px;
    border-left: 1px solid var(--rule-grey);
    font-size: 10.5px;
    font-style: normal;
    line-height: 15px;
    color: var(--text-grey);
  }
  .page-mark {
    position: absolute;
    left: 237px;
    top: 400px;
    width: 290px;
    height: 290px;
  }
</style>
</head>
<body>
  <main class="canvas">
    <section class="letterhead">
      <header class="brand">
        <div class="brand-line">
          <span class="brand-dot"></span>
          <span class="brand-name">Valtessora</span>
        </div>
        <span class="brand-tagline">Clínica de Movimento Humano</span>
      </header>

      <address class="contact-block">
        Endereço: Rua Aurora das Flores, 999<br>
        Cep: 99999-99 - Nonononio - MG<br>
        Fone: (31) 4820-5173<br>
        contato@valtessora.com<br>
        www.valtessora.com
      </address>

      <svg class="page-mark" viewBox="0 0 290 290" aria-hidden="true">
        <circle cx="145" cy="145" r="145" fill="var(--mark-grey)"/>
      </svg>
    </section>
  </main>
</body>
</html>
```